Create a Graphic About YOURSELF and PixelHarbor

PixelHarbor would like you (designers) to create an awesome graphic to promote YOURSELF and your profile on PixelHarbor!

Your graphic should communicate your name, your services and should mention PixelHarbor.

The design should be perfect for sharing on Chatterly. Here's an example of what we'd like http://blog.pixelharbor-example.ca/article/333/pixelharbor-launches-3000-hire-me-social-design-contest

Once you submitted your design, we'd love you to share the design ('advertisement') and promote yourself and PixelHarbor to your friends and potential customers. So make your submissions great and get your friends to vote for your design by 'Liking' it on Chatterly!

Prizes:
$1500 - "PixelHarbor Community" prize awarded to the designer with the most Chatterly 'Likes'
5 x $50 for the next 5 'most liked' designs on Chatterly

$1000 - "Hire Me" prize awarded to the designer who receives the most client invites
5 x $50 for the next 5 'most invited' designers

In summary, this is a great opportunity for you to increase your exposure to PixelHarbor customers and win cash prizes. Show off your design skills and get hired by PixelHarbor customers from around the world!

Target Market(s)

Fans, friends and customers of YOU

Industry/Entity Type

Cash

Requirements
Must have
• 1) Include your PixelHarbor user name on the graphic so customers can find you in the PixelHarbor Designer Directory
2) Include the tagline "Hire Me on PixelHarbor.com!" in your graphic design.
3) Share your design's URL on our Chatterly wall at http://chatterly-example.com/pixelharbor and get your friends to 'like' your design.
Nice to have
• 1) Include a tagline that expresses your design approach/philosophy
2) Artwork dimensions: 403 x 403 px
3) You can submit more than 1 design!
Should not have
• You must own the copyright of any images you use including stock imagery.

```html
<!DOCTYPE html>
<html lang="en">
<head>
<meta charset="utf-8">
<title>MARLO555 design – PixelHarbor</title>
<link rel="stylesheet" href="https://fonts.googleapis.com/css2?family=Audiowide&family=Source+Sans+3:wght@600;700&display=swap">
<style>
  :root {
    --paper-light: #dcb862;
    --paper-mid: #cfa64c;
    --paper-dark: #b98f3a;
    --title-pink: #f07ef0;
    --title-blue: #7d82f2;
    --title-edge: #2a1a2e;
    --design-pink: #e36be6;
    --design-shadow: #8b2f9b;
    --brand-blue: #17628f;
    --rule: rgba(255, 250, 230, 0.7);
  }
  * { margin: 0; padding: 0; box-sizing: border-box; }
  html, body {
    width: 1200px; height: 750px; overflow: hidden;
    background: var(--paper-mid);
  }
  .canvas {
    position: relative;
    width: 1200px; height: 750px; overflow: hidden;
    background:
      radial-gradient(ellipse at 50% 40%, var(--paper-light) 0%, var(--paper-mid) 60%, var(--paper-dark) 100%);
  }
  .floral-ornament {
    position: absolute;
    left: 45px; top: 80px;
    width: 1125px; height: 480px;
  }
  .tagline {
    position: absolute;
    left: 0; width: 1200px; top: 26px;
    text-align: center;
    font-family: "Source Sans 3", sans-serif;
    font-weight: 700;
    font-size: 42px; line-height: 1;
    color: var(--brand-blue);
    letter-spacing: 1px;
  }
  .designer-name {
    position: absolute;
    left: 0; width: 1200px; top: 218px;
    text-align: center;
    font-family: "Audiowide", sans-serif;
    font-size: 150px; line-height: 1;
    letter-spacing: 12px;
    padding-left: 12px;
    background: linear-gradient(90deg, var(--title-pink) 0%, var(--title-pink) 45%, var(--title-blue) 65%, var(--title-blue) 100%);
    -webkit-background-clip: text; background-clip: text;
    color: transparent;
    -webkit-text-stroke: 3px var(--title-edge);
    filter: drop-shadow(4px 6px 0 rgba(20, 10, 20, 0.55));
  }
  .designer-role {
    position: absolute;
    left: 0; width: 1216px; top: 380px;
    text-align: center;
    font-family: "Audiowide", sans-serif;
    font-size: 112px; line-height: 1;
    color: var(--design-pink);
    text-shadow: 3px 5px 0 var(--design-shadow), 6px 9px 6px rgba(40, 10, 50, 0.45);
  }
  .brand {
    position: absolute;
    left: 165px; top: 524px;
    display: flex; align-items: center; gap: 20px;
  }
  .brand-dot {
    width: 118px; height: 118px; border-radius: 50%;
    background: var(--brand-blue);
  }
  .brand-name {
    font-family: "Source Sans 3", sans-serif;
    font-weight: 600;
    font-size: 118px; line-height: 1;
    color: var(--brand-blue);
    letter-spacing: -1px;
  }
  .services {
    position: absolute;
    left: 0; width: 1244px; top: 656px;
    text-align: center;
    font-family: "Source Sans 3", sans-serif;
    font-weight: 700;
    font-size: 62px; line-height: 1;
    color: var(--brand-blue);
    letter-spacing: 1px;
  }
  .bottom-rule {
    position: absolute;
    left: 0; top: 731px; width: 1200px; height: 2px;
    background: var(--rule);
  }
</style>
</head>
<body>
  <main class="canvas">
    <svg class="floral-ornament" role="img" aria-label="Black floral swirl ornament with leaves, vines and ink splatters spreading behind the title" viewBox="0 0 1125 480" preserveAspectRatio="none">
      <defs>
        <radialGradient id="ornamentTone" cx="50%" cy="45%" r="55%">
          <stop offset="0%" stop-color="#2a1d0c" stop-opacity="0.28"/>
          <stop offset="60%" stop-color="#2a1d0c" stop-opacity="0.14"/>
          <stop offset="100%" stop-color="#2a1d0c" stop-opacity="0"/>
        </radialGradient>
      </defs>
      <rect width="1125" height="480" fill="url(#ornamentTone)"/>
    </svg>

    <p class="tagline">Hire Me on PixelHarbor.com!</p>

    <h1 class="designer-name">MARLO555</h1>
    <p class="designer-role">design</p>

    <div class="brand">
      <span class="brand-dot"></span>
      <span class="brand-name">PixelHarbor</span>
    </div>

    <p class="services">brochure website logo</p>
    <div class="bottom-rule"></div>
  </main>
</body>
</html>
```